Clean Energy Brand - Business Card and Letterhead Designs

Hi, everyone! We need a graphic designer who has experience working with the energy sector. We want help designing a perfect two-sided business card and letterhead for a clean energy company we've been assisting. We have a great new logo and all of the associated files.Our client is looking for a design that is "disruptive," "future-facing," "masculine," "bold," and "empowering." The colours of the logo are navy blue and orange and are meant to stand out. We'll need all ownership and copyright paperwork as well as first proofs in a 48-hour period.

Target Market(s)

Government; Non-Profits; Clean Energy Industry; Municipalities; North American Energy Sector

Industry/Entity Type

Power Generation

Requirements
Must have
• A matching business card and letterhead design
Should not have
• Must not be from a template

```html
<!DOCTYPE html>
<html lang="en">
<head>
<meta charset="utf-8">
<title>Kestrel Clean Energy – Stationery</title>
<link href="https://fonts.googleapis.com/css2?family=Exo+2:wght@500&family=Arimo:wght@400;700&display=swap" rel="stylesheet">
<style>
  :root {
    --navy: #0d2169;
    --orange: #f45a25;
    --band-grey: #e9eaeb;
    --text-grey: #555a60;
    --paper: #ffffff;
    --backdrop: #e4e5ea;
  }
  html, body {
    margin: 0;
    padding: 0;
    width: 1200px;
    height: 1041px;
    overflow: hidden;
    background: var(--backdrop);
  }
  .canvas {
    position: relative;
    width: 1200px;
    height: 1041px;
    font-family: "Arimo", Arial, sans-serif;
  }
  .letterhead, .card {
    position: absolute;
    background: var(--paper);
    overflow: hidden;
  }
  .letterhead { left: 102px; top: 99px; width: 663px; height: 855px; }
  .card { width: 273px; height: 158px; }
  .card--front { left: 830px; top: 99px; background: var(--navy); }
  .card--back { left: 830px; top: 283px; }
  .corner { position: absolute; display: block; }
  .brand-name {
    font-family: "Exo 2", "Trebuchet MS", sans-serif;
    font-weight: 500;
    color: var(--navy);
    margin: 0;
    line-height: 1;
  }
  .letterhead .brand { position: absolute; left: 53px; top: 92px; }
  .letterhead .brand-name { font-size: 34px; letter-spacing: -0.5px; }
  .letterhead .brand-tag { font-size: 12px; letter-spacing: 3px; margin-top: 6px; }
  .contact-footer {
    position: absolute;
    left: 366px; top: 768px; width: 228px;
    text-align: center;
  }
  .icon-row { display: flex; align-items: center; justify-content: center; gap: 8px; }
  .icon-row .rule { flex: 1; height: 1px; background: var(--navy); }
  .icon { width: 14px; height: 14px; display: block; }
  .contact-lines { margin-top: 9px; font-size: 8.5px; line-height: 10.5px; color: var(--text-grey); }
  .contact-lines .address { color: var(--navy); font-weight: 700; }
  .card--front .brand { position: absolute; right: 24px; top: 101px; text-align: right; }
  .card--front .brand-name { color: #ffffff; font-size: 21px; }
  .card--front .brand-tag { font-size: 7.5px; letter-spacing: 2px; margin-top: 3px; }
  .name-band {
    position: absolute; left: 0; top: 41px; width: 100%; height: 26px;
    background: var(--band-grey);
  }
  .person { position: absolute; left: 17px; top: 45px; }
  .person-name { margin: 0; font-size: 8.5px; font-weight: 700; color: var(--navy); }
  .person-title { margin: 1px 0 0; font-size: 7px; color: var(--text-grey); }
  .card--back .brand { position: absolute; left: 163px; width: 100px; top: 18px; text-align: center; }
  .brand-dot { display: block; width: 9px; height: 9px; border-radius: 50%; background: var(--orange); margin: 0 auto 9px; }
  .card--back .brand-name { font-size: 15px; }
  .card--back .brand-tag { font-size: 5px; letter-spacing: 1.5px; margin-top: 2px; }
  .card-contact { position: absolute; left: 17px; top: 98px; font-size: 6.5px; color: var(--text-grey); }
  .card-contact .address { color: var(--navy); font-weight: 700; padding-bottom: 4px; border-bottom: 1px solid var(--navy); width: 169px; }
  .card-contact .row { display: flex; align-items: center; gap: 3px; margin-top: 4px; }
  .card-contact .row + .row { margin-top: 3px; }
  .mini-icon { width: 6px; height: 6px; display: block; }
  .gap { width: 8px; }
</style>
</head>
<body>
<div class="canvas">

  <section class="letterhead" aria-label="Letterhead">
    <svg class="corner" style="right:0;top:0" width="215" height="72" viewBox="0 0 215 72">
      <polygon points="32,0 215,0 215,58" fill="var(--orange)"/>
      <polygon points="10,0 26,0 98,28 104,26 215,62 215,68 102,32 96,34" fill="var(--navy)"/>
    </svg>

    <div class="brand">
      <p class="brand-name">kestrel</p>
      <p class="brand-name brand-tag">CLEAN ENERGY</p>
    </div>

    <footer class="contact-footer">
      <div class="icon-row">
        <span class="rule"></span>
        <svg class="icon" viewBox="0 0 14 14"><circle cx="7" cy="7" r="7" fill="var(--orange)"/><path d="M7 3.2a2.4 2.4 0 0 0-2.4 2.4c0 1.8 2.4 4.6 2.4 4.6s2.4-2.8 2.4-4.6A2.4 2.4 0 0 0 7 3.2z" fill="#fff"/><circle cx="7" cy="5.6" r="0.9" fill="var(--orange)"/></svg>
        <svg class="icon" viewBox="0 0 14 14"><circle cx="7" cy="7" r="7" fill="var(--orange)"/><path d="M4.6 3.6l1.4-.3.8 1.8-.9.7a5 5 0 0 0 2.2 2.2l.7-.9 1.8.8-.3 1.4c-3 .3-6-2.7-5.7-5.7z" fill="#fff"/></svg>
        <svg class="icon" viewBox="0 0 14 14"><circle cx="7" cy="7" r="7" fill="var(--orange)"/><rect x="3.6" y="4.6" width="6.8" height="4.8" fill="#fff"/><path d="M3.6 4.6L7 7.3l3.4-2.7" fill="none" stroke="var(--orange)" stroke-width="0.7"/></svg>
        <svg class="icon" viewBox="0 0 14 14"><circle cx="7" cy="7" r="7" fill="var(--orange)"/><g fill="none" stroke="#fff" stroke-width="0.7"><circle cx="7" cy="7" r="3.5"/><ellipse cx="7" cy="7" rx="1.5" ry="3.5"/><path d="M3.5 7h7M4 5.2h6M4 8.8h6"/></g></svg>
        <span class="rule"></span>
      </div>
      <div class="contact-lines">
        <div class="address">24B Harbour Road West, Ridgeford, ON - K2P 4L9</div>
        <div>555-014-2267 &nbsp;|&nbsp; info@kestrelce.com</div>
        <div>www.kestrelce.com</div>
      </div>
    </footer>

    <svg class="corner" style="left:0;bottom:0" width="210" height="68" viewBox="0 0 210 68">
      <polygon points="0,9 0,68 188,68" fill="var(--orange)"/>
      <polygon points="0,0 96,31 102,29 210,68 196,68 100,35 94,37 0,6" fill="var(--navy)"/>
    </svg>
  </section>

  <section class="card card--front" aria-label="Business card front">
    <div class="brand">
      <p class="brand-name">kestrel</p>
      <p class="brand-name brand-tag">CLEAN ENERGY</p>
    </div>
  </section>

  <section class="card card--back" aria-label="Business card back">
    <div class="name-band"></div>
    <div class="person">
      <p class="person-name">DANA WHITFIELD</p>
      <p class="person-title">General Manager</p>
    </div>
    <div class="brand">
      <span class="brand-dot"></span>
      <p class="brand-name">kestrel</p>
      <p class="brand-name brand-tag">CLEAN ENERGY</p>
    </div>
    <div class="card-contact">
      <div class="row address">
        <svg class="mini-icon" viewBox="0 0 6 6"><path d="M3 0a2 2 0 0 0-2 2c0 1.5 2 4 2 4s2-2.5 2-4a2 2 0 0 0-2-2z" fill="var(--orange)"/><circle cx="3" cy="2" r="0.7" fill="#fff"/></svg>
        24B Harbour Road West, Ridgeford, ON - K2P 4L9
      </div>
      <div class="row">
        <svg class="mini-icon" viewBox="0 0 6 6"><path d="M1 0.4l1.2-.2.6 1.4-.7.6a4 4 0 0 0 1.7 1.7l.6-.7 1.4.6-.2 1.2C3 5.3.7 3 1 .4z" fill="var(--orange)"/></svg>
        555-014-2267<span class="gap"></span>
        <svg class="mini-icon" viewBox="0 0 6 6"><rect x="0" y="1" width="6" height="4" fill="var(--orange)"/><path d="M0 1l3 2.2L6 1" fill="none" stroke="#fff" stroke-width="0.6"/></svg>
        dana@kestrelce.com
      </div>
      <div class="row">
        <svg class="mini-icon" viewBox="0 0 6 6"><g fill="none" stroke="var(--orange)" stroke-width="0.6"><circle cx="3" cy="3" r="2.6"/><ellipse cx="3" cy="3" rx="1.1" ry="2.6"/><path d="M0.4 3h5.2"/></g></svg>
        www.kestrelce.com
      </div>
    </div>
    <svg class="corner" style="left:0;bottom:0" width="273" height="16" viewBox="0 0 273 16">
      <polygon points="0,1 142,1 146,0 273,0 273,4 148,4 144,7 0,7" fill="var(--orange)"/>
      <polygon points="0,7 144,7 148,4 273,4 273,16 0,16" fill="var(--navy)"/>
    </svg>
  </section>

</div>
</body>
</html>
```